PowerPoint Template Briefing for VALDRIK

Create a professional, consistent PowerPoint template in 16:9 format that adheres to VALDRIK's corporate identity guidelines. This template will be used regularly for client presentations, project proposals, and internal communications.

Template Requirements
- Format: 16:9 widescreen format for modern display compatibility
- Master slides to include:
- - Title slide with prominent logo placement
- - Section divider slides
- - Content slides with various layouts (text only, text with images, comparison layouts)
- - Data presentation slides (charts, tables, graphs)
- - Quote/testimonial slide
- - Contact/closing slide

Brand Elements Integration
- Logo placement: Consistent positioning on all slides (preferably top left or bottom right)
- Use both logo variations appropriately (text under icon for title slides, text right of icon for content slides)
- Color scheme: Implement the VALDRIK color palette throughout:
- - Primary Dark Gray (#404040) for main text and headers
- - Primary Blue (#295F7C) for accents and highlights
- - Highlight Blue (#3B8AB4) for call-outs and emphasis
- Typography: Montserrat font family exclusively, with appropriate size hierarchy:
- - Slide titles: Montserrat Bold
- - Headings: Montserrat SemiBold
- - Body text: Montserrat Regular
- - Captions/footnotes: Montserrat Light

Design Elements
- Clean, minimalist design with ample white space
- Subtle background elements that evoke global connectivity and time zones
- Modern, professional look aligned with IT industry standards
- Consistent footer with slide numbers and optional space for confidentiality notices
- Custom bullet points and dividers using brand colors

Technical Specifications
- Compatible with PowerPoint 2016 and newer versions
- Embedded Montserrat font or fallback instructions
- Editable text boxes and image placeholders
- Properly set up slide masters and layouts
- Optimized file size for easy sharing

Deliverables
- .POTX template file
- Brief usage guidelines for the template
- Sample slides demonstrating various layouts and proper usage

This template should serve as the foundation for all VALDRIK presentations, ensuring brand consistency while providing flexibility for various content needs.undefined

```html
<!DOCTYPE html>
<html lang="en">
<head>
<meta charset="utf-8">
<title>VALDRIK Presentation Template</title>
<link href="https://fonts.googleapis.com/css2?family=Montserrat:ital,wght@0,300;0,400;0,500;0,600;0,700;0,800;1,600;1,700&display=swap" rel="stylesheet">
<style>
  :root{
    --dark-gray:#404040;
    --primary-blue:#295F7C;
    --highlight-blue:#3B8AB4;
    --navy:#0e2238;
    --navy-mid:#183a57;
    --board:#cadcee;
    --board-light:#e3eef8;
    --white:#ffffff;
    --muted:#7a7f86;
    --rule:#d5dde5;
  }
  *{box-sizing:border-box;margin:0;padding:0}
  html,body{width:882px;height:1200px;overflow:hidden}
  body{
    font-family:"Montserrat",sans-serif;
    color:var(--dark-gray);
    background:radial-gradient(circle at 80% 15%,var(--board-light) 0,var(--board) 55%,#bcd2e8 100%);
    position:relative;
  }
  .slide{
    position:absolute;width:380px;height:214px;overflow:hidden;
    background:var(--white);
    box-shadow:0 4px 14px rgba(20,50,80,.18);
  }
  .slide.dark{background:var(--navy)}
  .col-left{left:50px}.col-right{left:452px}
  .row-1{top:30px}.row-2{top:262px}.row-3{top:494px}.row-4{top:726px}.row-5{top:958px}

  .photo{position:absolute;background:linear-gradient(135deg,#0b1b2e 0%,#1d4a6b 55%,#3B8AB4 100%)}
  .photo.light{background:linear-gradient(135deg,#f3f7fb 0%,#d7e6f2 60%,#a9c8df 100%)}
  .photo.full{inset:0}

  .logo{position:absolute;top:12px;right:14px;display:flex;align-items:center;gap:4px;
    font-weight:700;font-size:9px;letter-spacing:.06em;color:var(--primary-blue)}
  .logo .mark{width:9px;height:9px;border-radius:50%;background:var(--highlight-blue)}
  .logo.on-dark{color:var(--white)}
  .logo.stacked{flex-direction:column;gap:3px;font-size:10px}
  .logo.stacked .mark{width:14px;height:14px}

  .kicker{font-size:6.5px;font-weight:700;letter-spacing:.08em;color:var(--highlight-blue);text-transform:uppercase}
  .title{font-size:17px;font-weight:700;line-height:1.05;color:var(--dark-gray)}
  .title .accent{color:var(--highlight-blue)}
  .body{font-size:5px;line-height:1.55;color:var(--muted)}
  .body p+p{margin-top:4px}
  .footer{position:absolute;left:18px;right:14px;bottom:8px;display:flex;justify-content:space-between;
    font-size:4.5px;color:var(--muted);border-top:.6px solid var(--rule);padding-top:3px}
  .dark .footer{border-color:rgba(255,255,255,.2);color:rgba(255,255,255,.6)}

  .callout{position:absolute;background:var(--highlight-blue);color:var(--white);
    font-size:5px;line-height:1.5;padding:7px 8px}
  .callout strong{display:block;font-size:6.5px;font-weight:600;margin-bottom:2px}

  /* Slide 1 */
  .hero-title{position:absolute;left:22px;top:56px;color:var(--white);font-weight:700;font-size:22px;line-height:1.12}
  .hero-title .tag{display:inline-block;background:var(--highlight-blue);padding:0 5px;font-size:18px}

  /* Slide 2 */
  .intro-title{position:absolute;left:22px;top:100px;width:170px}
  .intro-copy{position:absolute;left:205px;top:42px;width:155px}

  /* Content slides */
  .head{position:absolute;left:20px;top:26px}
  .head .title{margin-top:2px}
  .copy{position:absolute;left:20px;width:150px}

  .feature-row{position:absolute;left:20px;right:18px;top:128px;display:grid;grid-template-columns:repeat(4,1fr);gap:10px}
  .feature .icon{width:14px;height:14px;border-radius:3px;background:var(--primary-blue);margin-bottom:4px}
  .feature h4{font-size:5.5px;font-weight:600;color:var(--dark-gray);margin-bottom:2px}

  .chart-label{position:absolute;font-size:4.5px;color:var(--muted);width:60px;line-height:1.4}
  .chart-label b{display:block;color:var(--primary-blue);font-size:6px}

  .bars text{font-family:"Montserrat",sans-serif}

  .stories{position:absolute;left:170px;top:30px;width:190px;display:flex;flex-direction:column;gap:6px}
  .story{background:var(--primary-blue);color:var(--white);font-size:4.8px;line-height:1.5;padding:6px 8px}
  .story:nth-child(2){background:var(--highlight-blue)}
  .story strong{display:block;font-size:6px;font-weight:600;margin-bottom:1px}

  .break-title{position:absolute;left:24px;top:120px;color:var(--white)}
  .break-title h2{font-size:24px;font-weight:700;line-height:1}
  .break-title .tag{display:inline-block;margin-top:5px;background:var(--highlight-blue);font-size:15px;font-weight:500;letter-spacing:.04em;padding:2px 8px}

  .thanks{position:absolute;left:190px;top:36px;width:170px}
  .thanks h2{font-size:22px;font-weight:700;font-style:italic;color:var(--highlight-blue)}
  .contacts{position:absolute;left:20px;right:18px;top:160px;display:grid;grid-template-columns:1fr 1fr;gap:5px 12px;
    font-size:5.5px;color:var(--dark-gray)}
  .contacts div{display:flex;align-items:center;gap:4px}
  .contacts svg{width:8px;height:8px;flex:none}
</style>
</head>
<body>

<!-- Title slide -->
<section class="slide dark col-left row-1">
  <div class="photo full" role="img" aria-label="Dark blue abstract technology image with a glowing X shape"></div>
  <div class="logo stacked on-dark"><span class="mark"></span>VALDRIK</div>
  <h1 class="hero-title">Bridging<br>Timezones<br>&amp; <span class="tag">DELIVERING</span><br>IT Excellence</h1>
</section>

<!-- Introduction slide -->
<section class="slide col-right row-1">
  <div class="photo light" style="left:0;top:0;width:150px;height:95px" role="img" aria-label="Connected network globe illustration in light blue"></div>
  <div class="logo"><span class="mark"></span>VALDRIK</div>
  <h2 class="title intro-title">Connecting<br>Expertise with<br><span class="accent">Innovation</span></h2>
  <div class="body intro-copy">
    <p>VALDRIK is a forward-thinking IT services company delivering global solutions across time zones with dedicated, reliable and expert teams.</p>
    <p>With a consistent and flexible approach, we help clients modernise systems, optimise processes and scale with confidence worldwide.</p>
    <p>Our teams combine deep technical knowledge with clear communication to deliver lasting value.</p>
  </div>
  <div class="footer"><span>VALDRIK</span><span>02</span></div>
</section>

<!-- Text with image -->
<section class="slide col-left row-2">
  <div class="logo"><span class="mark"></span>VALDRIK</div>
  <div class="head"><div class="kicker">Lorem Ipsum</div><h2 class="title">Lorem <span class="accent">Ipsum</span></h2></div>
  <div class="body copy" style="top:70px">
    <p>Lorem ipsum dolor sit amet, consectetur adipiscing elit, sed do eiusmod tempor incididunt ut labore et dolore magna aliqua.</p>
    <p>Ut enim ad minim veniam, quis nostrud exercitation ullamco laboris nisi ut aliquip ex ea commodo consequat.</p>
  </div>
  <div class="photo" style="left:190px;top:36px;width:172px;height:110px" role="img" aria-label="Hands typing on a keyboard with digital overlay"></div>
  <div class="callout" style="left:170px;top:132px;width:100px"><strong>Lorem ipsum dolor</strong>Sed ut perspiciatis unde omnis iste natus error sit.</div>
  <div class="footer"><span>VALDRIK</span><span>03</span></div>
</section>

<section class="slide col-right row-2">
  <div class="logo"><span class="mark"></span>VALDRIK</div>
  <div class="head"><div class="kicker">Lorem Ipsum</div><h2 class="title">Lorem <span class="accent">Ipsum</span></h2></div>
  <div class="body copy" style="top:70px">
    <p>Lorem ipsum dolor sit amet, consectetur adipiscing elit, sed do eiusmod tempor incididunt ut labore et dolore.</p>
    <p>Duis aute irure dolor in reprehenderit in voluptate velit esse cillum dolore eu fugiat nulla pariatur.</p>
  </div>
  <div class="photo" style="left:200px;top:36px;width:162px;height:100px" role="img" aria-label="Person working at a laptop in a dark office"></div>
  <div class="callout" style="left:182px;top:128px;width:96px"><strong>Lorem ipsum dolor</strong>Excepteur sint occaecat cupidatat non proident.</div>
  <div class="footer"><span>VALDRIK</span><span>04</span></div>
</section>

<!-- Four-column layout -->
<section class="slide col-left row-3">
  <div class="logo"><span class="mark"></span>VALDRIK</div>
  <div class="head"><div class="kicker">Lorem Ipsum</div><h2 class="title">Lorem <span class="accent">Ipsum</span></h2></div>
  <div class="body copy" style="top:70px;width:110px">
    <p>Lorem ipsum dolor sit amet, consectetur adipiscing elit, sed do eiusmod tempor.</p>
  </div>
  <div class="photo" style="left:150px;top:30px;width:120px;height:85px" role="img" aria-label="Abstract blue X shape made of light"></div>
  <div class="feature-row">
    <div class="feature"><div class="icon"></div><h4>Lorem Ipsum</h4><p class="body">Dolor sit amet consectetur adipiscing elit.</p></div>
    <div class="feature"><div class="icon"></div><h4>Lorem Ipsum</h4><p class="body">Dolor sit amet consectetur adipiscing elit.</p></div>
    <div class="feature"><div class="icon"></div><h4>Lorem Ipsum</h4><p class="body">Dolor sit amet consectetur adipiscing elit.</p></div>
    <div class="feature"><div class="icon"></div><h4>Lorem Ipsum</h4><p class="body">Dolor sit amet consectetur adipiscing elit.</p></div>
  </div>
  <div class="footer"><span>VALDRIK</span><span>05</span></div>
</section>

<!-- Donut chart -->
<section class="slide col-right row-3">
  <div class="logo"><span class="mark"></span>VALDRIK</div>
  <div class="photo" style="left:0;top:0;width:90px;height:110px" role="img" aria-label="Abstract blue X shape made of light"></div>
  <div style="position:absolute;left:100px;top:40px">
    <div class="kicker">Lorem Ipsum</div>
    <h2 class="title">Lorem<br><span class="accent">Ipsum</span></h2>
  </div>
  <div class="body copy" style="left:100px;top:90px;width:100px">
    <p>Lorem ipsum dolor sit amet, consectetur adipiscing elit, sed do eiusmod tempor incididunt.</p>
  </div>
  <svg style="position:absolute;left:250px;top:55px" width="100" height="100" viewBox="0 0 100 100">
    <g fill="none" stroke-width="14" transform="rotate(-90 50 50)">
      <circle cx="50" cy="50" r="34" stroke="#295F7C" stroke-dasharray="50 163.6"/>
      <circle cx="50" cy="50" r="34" stroke="#3B8AB4" stroke-dasharray="50 163.6" stroke-dashoffset="-53.4"/>
      <circle cx="50" cy="50" r="34" stroke="#0e2238" stroke-dasharray="50 163.6" stroke-dashoffset="-106.8"/>
      <circle cx="50" cy="50" r="34" stroke="#8fbcd8" stroke-dasharray="50 163.6" stroke-dashoffset="-160.2"/>
    </g>
    <circle cx="50" cy="50" r="18" fill="#e3eef8"/>
  </svg>
  <div class="chart-label" style="left:205px;top:50px"><b>25%</b>Lorem ipsum dolor</div>
  <div class="chart-label" style="left:205px;top:130px"><b>25%</b>Lorem ipsum dolor</div>
  <div class="footer"><span>VALDRIK</span><span>06</span></div>
</section>

<!-- Bar chart -->
<section class="slide col-left row-4">
  <div class="logo"><span class="mark"></span>VALDRIK</div>
  <svg class="bars" style="position:absolute;left:18px;top:34px" width="170" height="150" viewBox="0 0 170 150">
    <line x1="0" y1="140" x2="170" y2="140" stroke="#d5dde5" stroke-width="1"/>
    <g font-size="7" font-weight="600" fill="#404040" text-anchor="middle">
      <rect x="10" y="67" width="16" height="73" fill="#295F7C"/><text x="18" y="63">55%</text>
      <rect x="28" y="84" width="16" height="56" fill="#3B8AB4"/><text x="36" y="80">40%</text>
      <rect x="58" y="55" width="16" height="85" fill="#295F7C"/><text x="66" y="51">62%</text>
      <rect x="76" y="100" width="16" height="40" fill="#3B8AB4"/><text x="84" y="96">30%</text>
      <rect x="106" y="30" width="16" height="110" fill="#295F7C"/><text x="114" y="26">80%</text>
      <rect x="124" y="58" width="16" height="82" fill="#3B8AB4"/><text x="132" y="54">60%</text>
    </g>
  </svg>
  <div class="photo" style="left:150px;top:10px;width:50px;height:38px" role="img" aria-label="Small abstract blue X shape"></div>
  <div style="position:absolute;left:210px;top:55px"><div class="kicker">Lorem Ipsum</div><h2 class="title">Lorem <span class="accent">Ipsum</span></h2></div>
  <div class="body copy" style="left:210px;top:95px;width:150px">
    <p>Lorem ipsum dolor sit amet, consectetur adipiscing elit, sed do eiusmod tempor incididunt ut labore.</p>
    <p>Ut enim ad minim veniam, quis nostrud exercitation ullamco laboris.</p>
  </div>
  <div class="footer"><span>VALDRIK</span><span>07</span></div>
</section>

<!-- Testimonials -->
<section class="slide col-right row-4">
  <div class="logo"><span class="mark"></span>VALDRIK</div>
  <div class="head" style="top:60px"><div class="kicker">Lorem Ipsum</div><h2 class="title">Success<br><span class="accent">Stories</span></h2></div>
  <div class="body copy" style="top:110px;width:130px">
    <p>Lorem ipsum dolor sit amet, consectetur adipiscing elit sed do eiusmod.</p>
  </div>
  <div class="stories">
    <div class="story"><strong>Lorem Ipsum</strong>Lorem ipsum dolor sit amet, consectetur adipiscing elit, sed do eiusmod tempor.</div>
    <div class="story"><strong>Lorem Ipsum</strong>Lorem ipsum dolor sit amet, consectetur adipiscing elit, sed do eiusmod tempor.</div>
    <div class="story"><strong>Lorem Ipsum</strong>Lorem ipsum dolor sit amet, consectetur adipiscing elit, sed do eiusmod tempor.</div>
  </div>
  <div class="footer"><span>VALDRIK</span><span>08</span></div>
</section>

<!-- Section divider -->
<section class="slide dark col-left row-5">
  <div class="photo full" role="img" aria-label="Dark blue abstract technology image with glowing X shapes"></div>
  <div class="logo on-dark"><span class="mark"></span>VALDRIK</div>
  <div class="break-title"><h2>Slide Break</h2><span class="tag">LOREM IPSUM</span></div>
</section>

<!-- Closing slide -->
<section class="slide col-right row-5">
  <div class="logo"><span class="mark"></span>VALDRIK</div>
  <div class="photo light" style="left:0;top:0;width:120px;height:70px" role="img" aria-label="Light blue network globe illustration"></div>
  <div class="body copy" style="top:85px;width:150px">
    <p>Lorem ipsum dolor sit amet, consectetur adipiscing elit, sed do eiusmod tempor incididunt ut labore et dolore magna aliqua.</p>
  </div>
  <div class="thanks">
    <h2>Thank you!</h2>
    <div class="body" style="margin-top:6px"><p>Lorem ipsum dolor sit amet, consectetur adipiscing elit, sed do eiusmod tempor incididunt ut labore.</p></div>
  </div>
  <div class="contacts">
    <div><svg viewBox="0 0 10 10"><path d="M2 1h2l1 2-1.2 1a5 5 0 0 0 2.2 2.2L7 5l2 1v2a1 1 0 0 1-1 1A7 7 0 0 1 1 2a1 1 0 0 1 1-1z" fill="#3B8AB4"/></svg>+1 555 014 2288</div>
    <div><svg viewBox="0 0 10 10"><rect x="1" y="2" width="8" height="6" rx="1" fill="none" stroke="#3B8AB4"/><path d="M1 2.5l4 3 4-3" fill="none" stroke="#3B8AB4"/></svg>hello@valdrik.com</div>
    <div><svg viewBox="0 0 10 10"><path d="M5 1a3 3 0 0 1 3 3c0 2.5-3 5-3 5S2 6.5 2 4a3 3 0 0 1 3-3z" fill="#3B8AB4"/><circle cx="5" cy="4" r="1" fill="#fff"/></svg>100 Harbor Lane, Suite 4</div>
    <div><svg viewBox="0 0 10 10"><circle cx="5" cy="5" r="4" fill="none" stroke="#3B8AB4"/><path d="M1 5h8M5 1c-2 2.5-2 5.5 0 8M5 1c2 2.5 2 5.5 0 8" fill="none" stroke="#3B8AB4" stroke-width=".7"/></svg>www.valdrik.com</div>
  </div>
</section>

</body>
</html>
```